A clean crisp business card for a Landscape Construction company. Designed to be easy to read contact/ info and also be appealing/interesting, unlike a traditional business card.

Industry/Entity Type

Landscape Construction

Contact Information for Business Card

Company name : Bramblecrest Landscape Construction, phone number: (877) 62Vales, website:Bramblecrestlandscapes.example, Email, sales@bramblecrestlandscapes.example

Requirements
Nice to have
• Luxurious finishes/ details…. Icons or emblems next to contact info
Should not have
• Clipart or general pictures

```html
<!DOCTYPE html>
<html lang="en">
<head>
<meta charset="utf-8">
<title>Bramblecrest Landscape Construction – Business Card</title>
<link rel="stylesheet" href="https://fonts.googleapis.com/css2?family=Cinzel:wght@500;600&family=Crimson+Text:wght@400&display=swap">
<style>
  :root {
    --stage: #727176;
    --brand-blue: #236ab5;
    --deep-blue: #1f5fa6;
    --leaf-green: #9cc83b;
    --leaf-glow: rgba(156, 200, 59, 0.85);
    --leaf-fade: rgba(156, 200, 59, 0);
    --paper: #ffffff;
    --silver: #c8ccd2;
    --ink-light: #ffffff;
  }
  * { box-sizing: border-box; margin: 0; padding: 0; }
  html, body {
    width: 1200px; height: 900px; overflow: hidden;
    background: var(--stage);
  }
  .sheet {
    width: 1200px; height: 900px;
    display: flex; flex-direction: column;
    align-items: center; justify-content: center; gap: 36px;
  }
  .card {
    position: relative;
    width: 720px; height: 411px;
    border-radius: 20px;
    overflow: hidden;
    box-shadow: 0 10px 24px rgba(0,0,0,0.35);
  }

  /* Front: solid blue with wordmark */
  .card--front {
    background: var(--brand-blue);
    display: flex; align-items: center; justify-content: center;
  }
  .wordmark {
    font-family: "Cinzel", serif;
    font-weight: 600;
    text-align: center;
    line-height: 1.15;
  }
  .wordmark__name { display: block; font-size: 50px; letter-spacing: 1px; }
  .wordmark__trade { display: block; font-size: 17px; letter-spacing: 5px; }
  .card--front .wordmark { color: var(--silver); }

  /* Back: white top, wave, blue contact band */
  .card--back { background: var(--paper); }
  .card__waves { position: absolute; inset: 0; }
  .card--back .wordmark {
    position: absolute; left: 0; right: 0; top: 70px;
    color: var(--deep-blue);
  }
  .card--back .wordmark__name { font-size: 46px; }
  .card--back .wordmark__trade {
    font-size: 15px; letter-spacing: 4.5px;
    color: var(--leaf-green);
  }

  .leaf-sprig {
    position: absolute; right: 0; top: 70px;
    width: 110px; height: 170px;
    background: radial-gradient(ellipse 50% 50% at 65% 50%, var(--leaf-glow), var(--leaf-fade) 100%);
  }

  .contacts {
    position: absolute; left: 120px; bottom: 48px;
    display: flex; align-items: center; gap: 22px;
    font-family: "Crimson Text", serif;
    color: var(--ink-light);
    font-size: 21px;
  }
  .contacts__divider {
    width: 2px; height: 58px; background: var(--ink-light); opacity: 0.85;
  }
  .contacts__list { display: flex; flex-direction: column; gap: 6px; }
  .contact { display: flex; align-items: center; gap: 10px; white-space: nowrap; }
  .contact__icon { width: 20px; height: 20px; flex: none; }
</style>
</head>
<body>
<main class="sheet">

  <section class="card card--front" aria-label="Business card front">
    <div class="wordmark">
      <span class="wordmark__name">Bramblecrest</span>
      <span class="wordmark__trade">Landscape Construction</span>
    </div>
  </section>

  <section class="card card--back" aria-label="Business card back">
    <svg class="card__waves" viewBox="0 0 720 411" preserveAspectRatio="none" aria-hidden="true">
      <path d="M0 305 C 200 370, 420 205, 720 160 L720 411 L0 411 Z" fill="var(--deep-blue)"/>
      <path d="M0 262 C 210 345, 410 180, 720 132 L720 150 C 410 200, 210 365, 0 288 Z" fill="var(--leaf-green)"/>
    </svg>

    <div class="leaf-sprig" role="img" aria-label="Green leaf sprig rising from the end of the wave"></div>

    <div class="wordmark">
      <span class="wordmark__name">Bramblecrest</span>
      <span class="wordmark__trade">Landscape Construction</span>
    </div>

    <div class="contacts">
      <div class="contact">
        <svg class="contact__icon" viewBox="0 0 24 24" aria-hidden="true">
          <path fill="#fff" d="M6.6 10.8a15.1 15.1 0 0 0 6.6 6.6l2.2-2.2a1 1 0 0 1 1-.25 11.4 11.4 0 0 0 3.6.57 1 1 0 0 1 1 1V20a1 1 0 0 1-1 1A17 17 0 0 1 3 4a1 1 0 0 1 1-1h3.5a1 1 0 0 1 1 1c0 1.25.2 2.45.57 3.57a1 1 0 0 1-.25 1z"/>
        </svg>
        <span>(877) 62Vales</span>
      </div>
      <span class="contacts__divider" aria-hidden="true"></span>
      <div class="contacts__list">
        <div class="contact">
          <svg class="contact__icon" viewBox="0 0 24 24" aria-hidden="true">
            <rect x="2" y="5" width="20" height="14" fill="none" stroke="#fff" stroke-width="2"/>
            <path d="M2 5l10 8 10-8" fill="none" stroke="#fff" stroke-width="2"/>
          </svg>
          <span>sales@bramblecrestlandscapes.example</span>
        </div>
        <div class="contact">
          <svg class="contact__icon" viewBox="0 0 24 24" aria-hidden="true">
            <g fill="none" stroke="#fff" stroke-width="1.8">
              <circle cx="12" cy="12" r="9.5"/>
              <ellipse cx="12" cy="12" rx="4.5" ry="9.5"/>
              <path d="M2.5 12h19M4 7h16M4 17h16"/>
            </g>
          </svg>
          <span>bramblecrestlandscapes.example</span>
        </div>
      </div>
    </div>
  </section>

</main>
</body>
</html>
```